Start-up consultancy in Healthcare Space requiring clean and crisp website design

I am the founder of a start-up consultancy to improve access to medicines and healthcare around the globe. My primary product are consulting services to both the public sector and the private sector to work on: improved healthcare delivery, the right price for medicines and addressing challenges in emerging markets. As the sector is fairly conservative, I need a clean and very professional website as is should signal competence in the sector. Therefore, I like shades of white and green but there should be a link to healthcare. Please see the logo that is featured on my business cards.

Target Market(s)

Ministry of Health, Pharmaceutical companies, Emerging Markets (Latin America, Middle East, Eastern Europe, Asia)

Industry/Entity Type

Healthcare

Coding

Coded - Design and coding required

Number of Pages Required

5+ page

Font styles to use
Serif

Colors

Designer to choose colors to be used in the design.

Requirements
Must have
• About Section
• Services Section
• Blog Section
• The website design should also portray the solution for access to healthcare and highlight my ability to help clients with that.
• The website will be hosted on a CMS and should therefore be easy to adjust. I would prefer wordpress but open to any suggestions as I have my own webspace.
• I quite like these websites:
• https://www.tevluma.com/why-tevluma
• https://home.quillfernwell.com/
Nice to have
• I like to see some creative thinking with the theme of healthcare.
Should not have
• The design should not feature too many hospitals or pills etc. as this is really not my focus.

```html
<!DOCTYPE html>
<html lang="en">
<head>
<meta charset="utf-8">
<title>Veridane Consulting – Access to Healthcare</title>
<link rel="stylesheet" href="https://fonts.googleapis.com/css2?family=Alegreya+SC:wght@400;700&family=PT+Serif:wght@400;700&family=Roboto:wght@500;700&display=swap">
<style>
:root{
  --green:#0b5a27;
  --paper:#ececec;
  --white:#ffffff;
  --ink:#1b1b1b;
  --body:#2c2c2c;
  --bar:#1e1e1e;
  --footer:#272727;
  --footer-text:#e6e6e6;
}
*{margin:0;padding:0;box-sizing:border-box}
html,body{width:1200px;height:2736px;overflow:hidden}
body{position:relative;background:var(--paper);font-family:"PT Serif",Georgia,serif;color:var(--body)}
.heading{font-family:"Roboto",Arial,sans-serif;font-weight:700;color:var(--ink);text-align:center;position:absolute;left:0;width:1200px;font-size:35px;line-height:1}
.lede{position:absolute;left:0;width:1200px;text-align:center;font-size:15.5px;line-height:23px;color:var(--body)}

/* header */
.site-header{position:absolute;left:0;top:0;width:1200px;height:115px;background:#f3f4f3;border-top:7px solid var(--green)}
.brand{position:absolute;left:188px;top:36px;display:flex;flex-direction:column;align-items:center;width:132px;font-family:"PT Serif",Georgia,serif;font-weight:700;color:var(--green)}
.brand-name{font-size:25px;line-height:1}
.brand-sub{font-size:9px;letter-spacing:4px;margin-top:4px}
.main-nav{position:absolute;left:620px;top:-7px;height:115px;display:flex}
.main-nav a{font-family:"Alegreya SC",Georgia,serif;font-size:14.5px;color:#4a4a4a;text-decoration:none;height:115px;display:flex;align-items:center;padding:0 22px 0 0;letter-spacing:.5px}
.main-nav a.active{background:var(--green);color:var(--white);padding:0 19px;margin-right:25px;font-weight:700}

/* hero */
.hero{position:absolute;left:0;top:115px;width:1200px;height:377px;background:linear-gradient(100deg,#c9cdc8 0%,#aab2a7 28%,#8fa59c 50%,#c7b2a5 75%,#d9d3cc 100%)}
.hero-title{position:absolute;left:0;width:1200px;top:96px;text-align:center;font-family:"Alegreya SC",Georgia,serif;font-weight:400;color:var(--white);font-size:54px;line-height:60px;letter-spacing:1px}
.hero-title strong{font-weight:700}
.hero-cta{position:absolute;left:443px;top:241px;width:314px;height:44px;border:2px solid var(--white);color:var(--white);font-family:"Alegreya SC",Georgia,serif;font-size:19px;letter-spacing:1.5px;display:flex;align-items:center;justify-content:center}

/* about */
.about-card{position:absolute;left:188px;top:595px;width:824px;height:220px;background:var(--white)}
.about-foot{position:absolute;left:232px;top:815px;width:780px;height:46px;background:var(--white)}
.about-title{position:absolute;left:213px;top:614px;font-family:"Roboto",Arial,sans-serif;font-weight:700;font-size:35px;color:var(--ink)}
.about-text{position:absolute;left:213px;top:657px;width:458px;font-size:15.5px;line-height:22.6px;color:var(--body)}
.read-more{position:absolute;left:250px;top:827px;font-size:15px;color:var(--body);border-bottom:1px solid #555;padding-bottom:2px}
.about-photo{position:absolute;left:693px;top:542px;width:266px;height:266px;background:linear-gradient(135deg,#c9a06d,#e9ddd0 45%,#5f6f86)}
.about-notch{position:absolute;left:906px;top:542px;width:53px;height:53px;background:var(--white)}

/* services */
.service{position:absolute;top:1034px;width:256px;height:168px}
.service-photo{width:100%;height:133px}
.service-label{height:35px;background:var(--bar);color:var(--white);font-size:15px;display:flex;align-items:center;justify-content:center}

/* blog */
.blog-band{position:absolute;left:0;top:1273px;width:1200px;height:624px;background:var(--white)}
.post{position:absolute;overflow:hidden;color:var(--white)}
.post-date{position:absolute;border:2px solid var(--white);display:flex;flex-direction:column;align-items:center;justify-content:center;font-family:"Roboto",Arial,sans-serif;line-height:1}
.post-date b{font-weight:700}
.post-date span{font-size:10px;margin-top:3px}
.post-title{position:absolute;font-family:"Roboto",Arial,sans-serif;font-weight:700;line-height:1.2}
.post-excerpt{position:absolute;font-size:12.5px;line-height:20px}
.post.large{width:398px;height:217px;top:1450px}
.post.large .post-date{left:22px;top:100px;width:38px;height:44px}
.post.large .post-date b{font-size:21px}
.post.large .post-title{left:78px;top:100px;font-size:17.5px;width:265px}
.post.large .post-excerpt{left:22px;top:157px;width:350px}
.post.small{width:254px;height:137px;top:1698px}
.post.small .post-date{left:20px;top:70px;width:34px;height:40px}
.post.small .post-date b{font-size:18px}
.post.small .post-title{left:66px;top:72px;font-size:14px;width:160px}

/* testimonials */
.quote-card{position:absolute;left:232px;top:2105px;width:737px;height:295px}
.quote-panel{position:absolute;left:0;top:0;width:359px;height:295px;background:var(--green);color:var(--white)}
.quote-name{position:absolute;left:43px;top:30px;font-family:"Roboto",Arial,sans-serif;font-weight:700;font-size:33px}
.quote-place{position:absolute;left:43px;top:71px;font-size:14px}
.quote-mark{position:absolute;font-family:"PT Serif",Georgia,serif;font-weight:700;font-size:64px;line-height:1}
.quote-text{position:absolute;left:71px;top:123px;width:225px;font-size:15px;line-height:22px}
.quote-photo{position:absolute;left:359px;top:0;width:378px;height:295px;background:linear-gradient(120deg,#eef1f3,#d8dbe0 45%,#c9c4bb 80%,#b99b70)}
.dots{position:absolute;left:552px;top:2417px;display:flex;gap:5px}
.dots i{width:13px;height:13px;border:1.5px solid #333;border-radius:50%;display:block}
.dots i.on{background:#222}

/* footer */
.site-footer{position:absolute;left:0;top:2492px;width:1200px;height:244px;background:var(--footer);color:var(--footer-text)}
.footer-col{position:absolute;top:28px}
.footer-col h4{font-family:"Roboto",Arial,sans-serif;font-weight:700;font-size:18px;color:var(--white);padding-bottom:6px;border-bottom:2px solid var(--white);display:inline-block;padding-right:30px}
.footer-col p,.footer-col li{font-size:15px;line-height:26px}
.footer-col ul{list-style:none;margin-top:12px}
.footer-col li::before{content:"›";margin-right:12px}
.news-input{width:257px;height:36px;border:1px solid #8a8a8a;background:#3a3a3a;color:#bdbdbd;font-size:13px;display:flex;align-items:center;padding-left:12px;margin-top:10px}
.news-btn{width:257px;height:37px;background:var(--green);color:var(--white);font-size:13px;display:flex;align-items:center;justify-content:center;margin-top:9px;letter-spacing:.5px}
</style>
</head>
<body>

<header class="site-header">
  <div class="brand">
    <div class="brand-name">Veridane</div>
    <div class="brand-sub">CONSULTING</div>
  </div>
  <nav class="main-nav">
    <a class="active" href="#">Home</a>
    <a href="#">About</a>
    <a href="#">Services</a>
    <a href="#">Blog</a>
    <a href="#">Contact</a>
  </nav>
</header>

<section class="hero" role="img" aria-label="Photo of health advisers meeting with public officials around a table">
  <h1 class="hero-title">Opening Access to<br>Better <strong>Healthcare</strong></h1>
  <div class="hero-cta">Request a consultation</div>
</section>

<section class="about">
  <div class="about-card"></div>
  <div class="about-foot"></div>
  <div class="about-photo" role="img" aria-label="Photo of a consultant presenting a health access plan"></div>
  <div class="about-notch"></div>
  <h2 class="about-title">About Us</h2>
  <p class="about-text">We help ministries of health and pharmaceutical companies widen access to medicines and care. Our team brings field experience from Latin America, the Middle East, Eastern Europe and Asia, turning complex policy, pricing and supply questions into clear, workable plans that reach patients faster and make every budget go further.</p>
  <a class="read-more">Read more ›</a>
</section>

<section class="services">
  <h2 class="heading" style="top:910px">Our Best Services</h2>
  <p class="lede" style="top:952px">Consulting for the public and private sector on the questions<br>that decide who can reach the medicines and care they need.</p>
  <div class="service" style="left:188px">
    <div class="service-photo" role="img" aria-label="Photo of a clinic team planning patient services" style="background:linear-gradient(120deg,#e7e9e6,#b9b2a6 60%,#7f8a79)"></div>
    <div class="service-label">Healthcare Delivery</div>
  </div>
  <div class="service" style="left:472px">
    <div class="service-photo" role="img" aria-label="Photo of analysts reviewing medicine price data" style="background:linear-gradient(120deg,#d8d4cc,#ece7df 50%,#a59c8e)"></div>
    <div class="service-label">Medicine Pricing</div>
  </div>
  <div class="service" style="left:757px">
    <div class="service-photo" role="img" aria-label="Photo of a busy city street in an emerging market" style="background:linear-gradient(120deg,#a78d6c,#c99a8e 55%,#c9b895)"></div>
    <div class="service-label">Emerging Markets</div>
  </div>
</section>

<section class="blog-band"></section>
<section class="blog">
  <h2 class="heading" style="top:1322px">Our Blog</h2>
  <p class="lede" style="top:1364px">Notes from our work with health ministries and industry partners.<br>Ideas on access, pricing and care delivery worldwide</p>

  <article class="post large" style="left:188px;background:linear-gradient(120deg,#3c4a34,#26331f 55%,#4c5b3e)" role="img" aria-label="Photo of a rural health post surrounded by greenery">
    <div class="post-date"><b>21</b><span>Mar</span></div>
    <h3 class="post-title">5 ways to strengthen primary care delivery</h3>
    <p class="post-excerpt">Strong primary care is the first door to medicines, yet many systems still struggle to...</p>
  </article>
  <article class="post large" style="left:613px;background:linear-gradient(120deg,#8e7a6c,#6f5d52 50%,#9b8a80)" role="img" aria-label="Photo of a pharmacist handing a prescription across a counter">
    <div class="post-date"><b>17</b><span>Mar</span></div>
    <h3 class="post-title">How fair pricing can widen access to medicines</h3>
    <p class="post-excerpt">What is a fair price? It balances public budgets, patient reach and a viable supply...</p>
  </article>

  <article class="post small" style="left:188px;background:linear-gradient(120deg,#7b7f83,#8e8b86 60%,#6c7075)" role="img" aria-label="Photo of a team on a video call across countries">
    <div class="post-date"><b>16</b><span>Mar</span></div>
    <h3 class="post-title">How to build a cross-border health team</h3>
  </article>
  <article class="post small" style="left:472px;background:linear-gradient(120deg,#9b928b,#b3aaa3 55%,#857b74)" role="img" aria-label="Photo of officials reviewing a budget report">
    <div class="post-date"><b>15</b><span>Mar</span></div>
    <h3 class="post-title">Can tiered pricing protect public budgets...?</h3>
  </article>
  <article class="post small" style="left:759px;background:linear-gradient(120deg,#3d4a33,#5b6650 55%,#7c7f74)" role="img" aria-label="Photo of a health worker outside a community clinic">
    <div class="post-date"><b>15</b><span>Mar</span></div>
    <h3 class="post-title">Lessons from Latin American health reform</h3>
  </article>
</section>

<section class="testimonials">
  <h2 class="heading" style="top:1952px">Testimonials</h2>
  <p class="lede" style="top:1993px">Our 97% client satisfaction rate is unparalleled in our field.<br>Read below what our clients have to say and learn more about what makes us<br>a trusted partner for access to medicines worldwide.</p>
  <div class="quote-card">
    <div class="quote-panel">
      <div class="quote-name">Marion T</div>
      <div class="quote-place">Deputy Director, Health Ministry</div>
      <div class="quote-mark" style="left:36px;top:98px">“</div>
      <p class="quote-text">your guidance on pricing and supply gave our ministry a clear path forward. our entire team thanks you for all you have done.</p>
      <div class="quote-mark" style="left:272px;top:228px">”</div>
    </div>
    <div class="quote-photo" role="img" aria-label="Photo of a consultant and a ministry official shaking hands in an office"></div>
  </div>
  <div class="dots"><i></i><i></i><i class="on"></i><i></i><i></i></div>
</section>

<footer class="site-footer">
  <div class="footer-col" style="left:188px">
    <h4>Contact Us</h4>
    <p style="margin-top:12px">88 linden park road. suite<br>210 fairhaven mu 302118<br>hello@veridaneconsulting.com<br>01 555 240 7710</p>
  </div>
  <div class="footer-col" style="left:514px">
    <h4>Quick Links</h4>
    <ul><li>About Us</li><li>Blog</li><li>Services</li><li>Contact</li></ul>
  </div>
  <div class="footer-col" style="left:753px">
    <h4>Email Newsletters</h4>
    <p style="margin-top:12px">sign up to receive the latest articles</p>
    <div class="news-input">Your Email Address</div>
    <div class="news-btn">SUBSCRIBE</div>
  </div>
</footer>

</body>
</html>
```